Corporate brochure design 4 pages

Hi,

We are a real estate company based in Europe.

We have almost finalized a rebranding.

We are developing a brand book guidelines (still on working process) to help you undertstand the look and feel of our new CI. I would like to receive proposals of design for a corporate brochure template. I need to receive the Indesign files with full ownership rights to be able to adapt all our documentation with this template.
Regarding the images, you can take gabaris on www.pelvaromedia.com. I will be able to take them afterwards.

There will be 4 pages. you will receive the 4 pages on pdf for your consideration with our (almost) actual layout.

- 1st page: cover
- 2nd page: company presentation in french and english
- 3rd page: some market data + graph
- 4th page: 2 retail centers presentation.

In the template, i need to have:
- the paragraph styles in order
- 2 different masters with top/bottom/page number aso.

Please feel free to ask any other questions.

best regards,
Updates

I would like to precise tha t we are active on the commercial real estate sector:

- office transactions (rent /sales)
- property management of administrative and business buildings
- Valuation of properties
- Capital markets (investment advices for selling building)

Industry/Entity Type

Real Estate

Colors

Designer to choose colors to be used in the design.

```html
<!DOCTYPE html>
<html lang="en">
<head>
<meta charset="utf-8">
<title>Corvane Commercial Real Estate – Retail Centres Spread</title>
<link rel="stylesheet" href="https://fonts.googleapis.com/css2?family=Montserrat:wght@300;700&family=Marcellus&family=Arimo&family=Archivo+Narrow&display=swap">
<style>
  :root {
    --orange: #f26a24;
    --ink: #231f20;
    --paper: #ffffff;
    --rule: #555555;
    --night-deep: #0b1030;
    --night-mid: #2a2f7a;
    --night-glow: #6a5aa8;
  }
  * { margin: 0; padding: 0; box-sizing: border-box; }
  html, body { width: 1200px; height: 928px; overflow: hidden; background: var(--paper); }
  .spread { position: relative; width: 1200px; height: 928px; background: var(--paper); overflow: hidden; }
  .top-band { position: absolute; top: 0; left: 0; width: 1200px; height: 12px; background: var(--orange); }
  .fold { position: absolute; top: 0; left: 599px; width: 1px; height: 928px; background: #9a9a9a; }

  /* Inside page */
  .photo-slot {
    position: absolute; top: 23px; width: 258px; height: 234px;
    background: var(--ink); color: #fff;
    display: flex; align-items: center; justify-content: center;
    font-family: "Marcellus", serif; font-size: 28px; letter-spacing: 1px;
  }
  .photo-slot--one { left: 39px; }
  .photo-slot--two { left: 315px; }

  .centre-labels { position: absolute; top: 259px; left: 45px; width: 522px; height: 64px; overflow: visible; }
  .centre-labels text { font-family: "Marcellus", serif; }

  .column {
    position: absolute; top: 335px; width: 260px;
    font-family: "Arimo", sans-serif; font-size: 13.3px; line-height: 16.2px; color: #111;
  }
  .column p + p { margin-top: 16px; }
  .column--left { left: 35px; }
  .column--right { left: 316px; }
  .column-rule { position: absolute; left: 305px; top: 339px; width: 1px; height: 496px; background: var(--rule); }

  .footer { position: absolute; left: 0; top: 847px; width: 600px; height: 81px; background: var(--ink); }
  .footer__web {
    position: absolute; left: 15px; top: 2px; width: 590px; height: 25px;
    background: var(--orange); border: 2px solid #fff; border-right: none;
    border-radius: 13px 0 0 13px;
    font-family: "Arimo", sans-serif; font-size: 16px; line-height: 21px; color: var(--ink);
    padding-left: 81px;
  }
  .footer__call {
    position: absolute; left: 134px; top: 30px; color: var(--orange);
    font-family: "Archivo Narrow", sans-serif; white-space: nowrap;
  }
  .footer__call-label { font-size: 28px; margin-right: 6px; }
  .footer__call-number { font-size: 40px; }

  /* Cover page */
  .brand { position: absolute; left: 600px; top: 190px; width: 600px; text-align: center; }
  .brand__name {
    font-family: "Montserrat", sans-serif; font-weight: 700; font-size: 98px;
    letter-spacing: -2px; line-height: 1; color: var(--ink);
  }
  .brand__tagline {
    margin-top: 16px;
    font-family: "Montserrat", sans-serif; font-weight: 300; font-size: 24px;
    letter-spacing: 6px; color: var(--orange);
  }
  .cover-art { position: absolute; left: 600px; top: 420px; width: 600px; height: 508px; }
</style>
</head>
<body>
<div class="spread">
  <div class="top-band"></div>

  <section class="page page--centres">
    <div class="photo-slot photo-slot--one">Photo 1</div>
    <div class="photo-slot photo-slot--two">Photo 2</div>

    <svg class="centre-labels" viewBox="0 0 522 64" aria-label="Retail Centre 1 and Retail Centre 2">
      <rect x="3" y="2" width="240" height="60" rx="30" fill="var(--ink)"/>
      <rect x="280" y="2" width="240" height="60" rx="30" fill="var(--orange)"/>
      <path class="badge badge--one" d="M260 2 H236 A30 30 0 0 0 236 62 H260 Z" fill="var(--orange)" stroke="#fff" stroke-width="3" stroke-linejoin="round"/>
      <path class="badge badge--two" d="M260 2 H287 A30 30 0 0 1 287 62 H260 Z" fill="var(--ink)" stroke="#fff" stroke-width="3" stroke-linejoin="round"/>
      <text x="24" y="43" font-size="28" fill="#fff">Retail Centre</text>
      <text x="235" y="47" font-size="40" fill="#fff" text-anchor="middle">1</text>
      <text x="287" y="47" font-size="40" fill="#fff" text-anchor="middle">2</text>
      <text x="333" y="41" font-size="28" fill="#fff">Retail Centre</text>
    </svg>

    <div class="column column--left">
      <p>Lorem ipsum dolor sit amet, consectetur adipisicing elit, sed do eiusmod tempor incididunt ut labore et dolore magna aliqua. Ut enim ad minim veniam, quis nostrud exercitation ullamco laboris nisi ut aliquip ex ea commodo consequa.Lorem ipsum dolor sit amet, consectetur adipisicing elit, sed do eiusmod tempor incididunt ut labore et dolore magna aliqua. Ut enim ad minim veniam, quis.</p>
      <p>Lorem ipsum dolor sit amet, consectetur adipisicing elit, sed do eiusmod tempor incididunt ut labore et dolore magna aliqua. Ut enim ad minim veniam, quis nostrud exercitation ullamco laboris nisi ut aliquip ex ea commodo consequa.Lorem ipsum dolor sit amet, consectetur adipisicing elit, sed do eiusmod tempor incididunt ut labore et dolore magna aliqua. Ut enim ad minim veniam, quis.</p>
      <p>Lorem ipsum dolor sit amet, consectetur adipisicing elit, sed do eiusmod tempor incididunt ut labore et dolore magna aliqua. Ut enim ad minim veniam, quis nostrud exercitation ullamco laboris nisi ut aliquip ex ea commodo consequa.Lorem ipsum dolor sit amet, consectetur adipisicing elit, sed do eiusmod tempor incididunt ut labore et dolore magna aliqua.</p>
    </div>
    <div class="column-rule"></div>
    <div class="column column--right">
      <p>Lorem ipsum dolor sit amet, consectetur adipisicing elit, sed do eiusmod tempor incididunt ut labore et dolore magna aliqua. Ut enim ad minim veniam, quis nostrud exercitation ullamco laboris nisi ut aliquip ex ea commodo consequa.Lorem ipsum dolor sit amet, consectetur adipisicing elit, sed do eiusmod tempor incididunt ut labore et dolore magna aliqua. Ut enim ad minim veniam, quis.</p>
      <p>Lorem ipsum dolor sit amet, consectetur adipisicing elit, sed do eiusmod tempor incididunt ut labore et dolore magna aliqua. Ut enim ad minim veniam, quis nostrud exercitation ullamco laboris nisi ut aliquip ex ea commodo consequa.Lorem ipsum dolor sit amet, consectetur adipisicing elit, sed do eiusmod tempor incididunt ut labore et dolore magna aliqua. Ut enim ad minim veniam, quis.</p>
      <p>Lorem ipsum dolor sit amet, consectetur adipisicing elit, sed do eiusmod tempor incididunt ut labore et dolore magna aliqua. Ut enim ad minim veniam, quis nostrud exercitation ullamco laboris nisi ut aliquip ex ea commodo consequa.Lorem ipsum dolor sit amet, consectetur adipisicing elit, sed do eiusmod tempor incididunt ut labore et dolore magna aliqua.</p>
    </div>

    <footer class="footer">
      <div class="footer__web">www.corvanecommercial.com</div>
      <div class="footer__call"><span class="footer__call-label">Call :</span><span class="footer__call-number">000 000 0000</span></div>
    </footer>
  </section>

  <section class="page page--cover">
    <div class="brand">
      <div class="brand__name">CORVANE</div>
      <div class="brand__tagline">COMMERCIAL REAL ESTATE</div>
    </div>

    <svg class="cover-art" viewBox="0 0 600 508" preserveAspectRatio="none">
      <defs>
        <linearGradient id="nightSky" x1="0" y1="0" x2="0" y2="1">
          <stop offset="0" stop-color="var(--night-deep)"/>
          <stop offset="0.45" stop-color="var(--night-mid)"/>
          <stop offset="0.75" stop-color="var(--night-glow)"/>
          <stop offset="0.88" stop-color="#3a2f40"/>
          <stop offset="1" stop-color="#0a0d22"/>
        </linearGradient>
      </defs>
      <path d="M0 5 Q300 70 600 32 L600 48 Q300 90 0 20 Z" fill="var(--orange)"/>
      <path d="M0 18 Q300 88 600 46 L600 508 L0 508 Z" fill="url(#nightSky)" role="img" aria-label="Photo of a city skyline with lit towers at night across the water"/>
    </svg>
  </section>

  <div class="fold"></div>
</div>
</body>
</html>
```